Business cards, letterheads, envelopes, notepad design

We are a new business in Miami, Florida. We produce business printing, signs and photogifts such as canvas prints, t shirts, mugs, phone cases etc.
Our store will be very modern with interactive stations for clients to design their own products on our cloud design software. We want something that will appeal to business clients and the general public clients.
We need designs for business cards, letterheads, notepads, and envelopes - all 4 colour process - full bleed OK.

Target Market(s)

We target both business clients and the general public.

Industry/Entity Type

Store

Font styles to use
Sans Serif
Other font styles liked:
• Harabara

Colors
acd036
33a6d7
e34197
000000

Requirements
Must have
• Cyan, Magenta, Lime Green
Should not have
• No cats. Absolutely.

```html
<!DOCTYPE html>
<html lang="en">
<head>
<meta charset="utf-8">
<title>Inkvale – Business Card</title>
<link rel="stylesheet" href="https://fonts.googleapis.com/css2?family=Open+Sans:wght@400;600;700;800&display=swap">
<style>
  :root {
    --lime: #acd036;
    --cyan: #33a6d7;
    --magenta: #e34197;
    --black: #000000;
    --ink: #1f1f1f;
    --text: #3a3a3a;
    --paper: #ffffff;
    --card-dark: #1b1b1b;
    --emboss: #101010;
    --stage: #2f2f2f;
  }
  * { box-sizing: border-box; margin: 0; padding: 0; }
  html, body { width: 1200px; height: 900px; overflow: hidden; }
  body {
    background: var(--stage);
    font-family: "Open Sans", Arial, sans-serif;
    position: relative;
  }
  .card {
    position: absolute;
    width: 540px;
    height: 309px;
    overflow: hidden;
  }
  /* front */
  .card-front { left: 60px; top: 110px; background: var(--paper); }
  .card-front .brand {
    position: absolute; left: 40px; top: 48px;
    display: flex; align-items: center; gap: 12px;
  }
  .brand-mark { width: 22px; height: 22px; background: var(--magenta); }
  .card-front .brand-name {
    font-weight: 800; font-size: 48px; color: var(--ink); letter-spacing: -1px;
  }
  .holder {
    position: absolute; right: 40px; top: 150px; text-align: right;
    font-weight: 700; font-size: 15px; letter-spacing: 1px; color: var(--ink);
  }
  .contact {
    position: absolute; left: 40px; top: 150px;
    list-style: none; font-size: 13px; line-height: 20px; color: var(--text);
  }
  .contact .key { font-weight: 700; }
  .key-phone { color: var(--lime); }
  .key-fax { color: var(--cyan); }
  .key-mail { color: var(--magenta); }
  .key-web { color: var(--ink); }
  .address {
    position: absolute; left: 230px; top: 200px;
    font-style: normal; font-size: 13px; line-height: 20px; color: var(--text);
  }
  .bands { position: absolute; left: 0; right: 0; bottom: 0; display: flex; }
  .band { flex: 1; }
  .band-lime { background: var(--lime); }
  .band-cyan { background: var(--cyan); }
  .band-magenta { background: var(--magenta); }
  .card-front .bands { height: 14px; }
  /* back */
  .card-back { left: 600px; top: 480px; background: var(--card-dark); }
  .card-back .brand {
    position: absolute; inset: 0 0 10px 0;
    display: flex; align-items: center; justify-content: center;
  }
  .card-back .brand-name {
    font-weight: 800; font-size: 84px; color: var(--emboss); letter-spacing: -2px;
  }
  .card-back .bands { height: 10px; }
</style>
</head>
<body>
  <section class="card card-front" aria-label="Business card front">
    <div class="brand">
      <span class="brand-mark"></span>
      <span class="brand-name">Inkvale</span>
    </div>
    <p class="holder">DANIEL REYES</p>
    <ul class="contact">
      <li><span class="key key-phone">P:</span> 844- 4INKVALE</li>
      <li><span class="key key-fax">F:</span> 844-555-0186</li>
      <li><span class="key key-mail">E:</span> daniel@inkvale.com</li>
      <li><span class="key key-web">W:</span> www.inkvale.com</li>
    </ul>
    <address class="address">
      Harborview Plaza,<br>
      240 NE 2nd Avenue #5<br>
      Miami, Florida 33131
    </address>
    <div class="bands">
      <span class="band band-lime"></span>
      <span class="band band-cyan"></span>
      <span class="band band-magenta"></span>
    </div>
  </section>

  <section class="card card-back" aria-label="Business card back">
    <div class="brand">
      <span class="brand-name">Inkvale</span>
    </div>
    <div class="bands">
      <span class="band band-lime"></span>
      <span class="band band-cyan"></span>
      <span class="band band-magenta"></span>
    </div>
  </section>
</body>
</html>
```